New Webpage for High Class Expert Witness Services Company

We are looking for a minimalist design for a webpage that just has our logo and an entry form offer to connect with one of our Liaisons.
The entry form should just ask for Name, Email, Contact Info and Description of Project.

Company Name is: The Marlow Crest Advisory Services

Number of Pages Required

1 page

```html
<!DOCTYPE html>
<html lang="en">
<head>
<meta charset="utf-8">
<title>Connect with a Liaison – The Marlow Crest Advisory Services</title>
<link href="https://fonts.googleapis.com/css2?family=Cinzel:wght@600;700&family=Poppins:wght@400&display=swap" rel="stylesheet">
<style>
  :root {
    --ink: #111111;
    --label: #1a1a1a;
    --icon: #8a8a8a;
    --field-bg: #f3f3f3;
    --field-border: #c9c9c9;
    --page-bg: #ffffff;
    --hero-dark: #1c231d;
    --hero-mid: #3b3a2c;
    --hero-olive: #5a5239;
    --hero-text: #ffffff;
  }
  * { box-sizing: border-box; margin: 0; padding: 0; }
  html, body { width: 1200px; height: 719px; overflow: hidden; background: var(--page-bg); }
  .page { position: relative; width: 1200px; height: 719px; }

  .hero {
    position: absolute; left: 0; top: 0; width: 517px; height: 719px;
    background:
      radial-gradient(ellipse at 55% 55%, var(--hero-olive) 0%, rgba(90,82,57,0) 60%),
      linear-gradient(160deg, var(--hero-dark) 0%, #2a3128 40%, var(--hero-mid) 75%, #4a3a26 100%);
  }
  .brand {
    position: absolute; left: 143px; top: 296px;
    display: flex; align-items: center; gap: 10px;
  }
  .brand-mark { width: 34px; height: 34px; background: var(--hero-text); }
  .brand-name {
    font-family: "Cinzel", serif; font-weight: 600; font-size: 21px;
    line-height: 1.15; color: var(--hero-text); letter-spacing: 0.5px;
  }
  .hero-notes {
    position: absolute; left: 143px; top: 369px;
    font-family: "Poppins", sans-serif; font-size: 13px; line-height: 20.5px;
    color: var(--hero-text); list-style: none;
  }

  .liaison {
    position: absolute; left: 578px; top: 0; width: 482px;
  }
  .liaison-title {
    position: absolute; left: -1px; top: 121px; white-space: nowrap;
    font-family: "Cinzel", serif; font-weight: 700; font-size: 37px;
    color: var(--ink); letter-spacing: 0.6px;
  }
  .field-label {
    position: absolute; left: 0; display: flex; align-items: center; gap: 10px;
    font-family: "Poppins", sans-serif; font-size: 13px; color: var(--label);
  }
  .field-label svg { width: 16px; height: 16px; fill: var(--icon); }
  .field-input {
    position: absolute; left: 0; width: 482px; height: 43px;
    background: var(--field-bg); border: 1px solid var(--field-border);
  }
  .field-input.is-area { height: 89px; }
  .submit {
    position: absolute; left: 0; top: 546px; width: 335px; height: 42px;
    background: var(--ink); color: var(--hero-text); border: none;
    font-family: "Cinzel", serif; font-weight: 600; font-size: 16.5px; letter-spacing: 0.4px;
  }
</style>
</head>
<body>
<main class="page">
  <section class="hero" role="img" aria-label="Photograph of an armed tactical operator in gear in a forest"></section>
  <div class="brand">
    <span class="brand-mark"></span>
    <span class="brand-name">The Marlow Crest<br>Advisory Services</span>
  </div>
  <ul class="hero-notes">
    <li>© The Marlow Crest Advisory Services</li>
    <li>- Secure Liaison Protocol</li>
    <li>- All Submissions Encrypted</li>
  </ul>

  <form class="liaison">
    <h1 class="liaison-title">Connect with a Liaison</h1>

    <label class="field-label" style="top:183px">
      <svg viewBox="0 0 16 16"><circle cx="8" cy="4.5" r="3.5"/><path d="M1 16c0-4 3-6.5 7-6.5s7 2.5 7 6.5z"/></svg>
      Full Name
    </label>
    <div class="field-input" style="top:206px"></div>

    <label class="field-label" style="top:262px">
      <svg viewBox="0 0 16 16"><path d="M0 7.5 16 1l-3 13-5-3.5-2 3v-4.5L13 3 5 9z"/></svg>
      Email Address
    </label>
    <div class="field-input" style="top:285px"></div>

    <label class="field-label" style="top:341px; gap:7px">
      <svg viewBox="0 0 16 16"><path d="M3.5 1 6 4 4.5 6c1 2 3 4 5.5 5.5l2-1.5 3 2.5-1.5 2.5C8 15 1 8 1 2.5z"/><path d="M9 1a6 6 0 0 1 6 6h-1.3A4.7 4.7 0 0 0 9 2.3zM9 4a3 3 0 0 1 3 3h-1.3A1.7 1.7 0 0 0 9 5.3z"/></svg>
      Contact info (phone / secure line)
    </label>
    <div class="field-input" style="top:364px"></div>

    <label class="field-label" style="top:420px">
      <svg viewBox="0 0 16 16"><path d="M1 2h10v3l-5 5-1 3h6v-2l2-2v6H1z"/><path d="M3 5h6v1H3zM3 7.5h4v1H3z" fill="#fff"/><path d="M14 4l1.5 1.5-7 7H7v-1.5z"/></svg>
      Description of Project
    </label>
    <div class="field-input is-area" style="top:442px"></div>

    <button class="submit" type="button">Request Liaison Connection</button>
  </form>
</main>
</body>
</html>
```